I need the following on my business card:
- Name: Dana Whitcomb
- License # 0M93216
- Title: Producer
- Phone: (555) 017-3904
- Email: Dana@CorbelInsuranceServices.com

- Company: Corbel Insurance Services
- Address: 27408 Larkmoor Ave Suite 610, Sherman Oaks, CA 90217
- Website: www.CorbelInsuranceServices.com

Also add our slogan on the card: "Where Trust Meets Coverage"

```html
<!DOCTYPE html>
<html lang="en">
<head>
<meta charset="utf-8">
<title>Corbel Insurance Services – Business Card</title>
<link href="https://fonts.googleapis.com/css2?family=Lato:wght@300;400;700;900&display=swap" rel="stylesheet">
<style>
  :root {
    --navy: #0a2a8a;
    --green: #1f9a3a;
    --ink: #333a44;
    --rule: #3a56a8;
    --paper: #ffffff;
    --backdrop: #e6e7ea;
  }
  * { box-sizing: border-box; margin: 0; padding: 0; }
  html, body { width: 1200px; height: 900px; overflow: hidden; }
  body {
    background: var(--backdrop);
    font-family: "Lato", Arial, sans-serif;
    display: flex;
    align-items: center;
    justify-content: center;
    gap: 70px;
  }
  .card { box-shadow: 0 10px 30px rgba(0,0,0,.18); position: relative; }

  /* Front */
  .card-front {
    width: 630px; height: 360px;
    background: var(--navy);
    display: flex; flex-direction: column;
    align-items: center; justify-content: center;
  }
  .brand-name {
    color: #fff;
    font-weight: 900;
    font-size: 46px;
    letter-spacing: 1px;
    text-transform: uppercase;
    text-align: center;
    line-height: 1.1;
  }
  .tagline {
    margin-top: 58px;
    display: flex; align-items: center; gap: 14px;
    color: #fff; font-weight: 700; font-size: 17px; letter-spacing: .3px;
  }
  .tagline::before, .tagline::after {
    content: ""; width: 110px; height: 1px; background: var(--green);
  }

  /* Back */
  .card-back {
    width: 360px; height: 630px;
    background: var(--paper);
    display: flex; flex-direction: column; align-items: center;
    padding-top: 150px; text-align: center;
  }
  .holder-name {
    color: var(--navy); font-weight: 900; font-size: 31px;
    text-transform: uppercase; letter-spacing: .5px;
  }
  .holder-license { color: var(--navy); font-weight: 300; font-size: 19px; margin-top: 2px; }
  .holder-title { color: var(--green); font-size: 19px; margin-top: 2px; }

  .divider {
    display: flex; align-items: center; gap: 10px;
    width: 270px; margin: 26px 0 18px;
  }
  .divider::before, .divider::after {
    content: ""; flex: 1; height: 1.5px; background: var(--rule);
  }
  .icon-row { display: flex; gap: 3px; }
  .icon {
    width: 26px; height: 26px; background: var(--green);
    display: flex; align-items: center; justify-content: center;
  }
  .icon svg { width: 16px; height: 16px; }

  .company { color: var(--navy); font-weight: 700; font-size: 17px; }
  .address { color: var(--ink); font-size: 16px; line-height: 1.35; margin-top: 2px; }
  .phone { color: var(--ink); font-size: 25px; font-weight: 400; }
  .web { color: var(--ink); font-size: 14.5px; line-height: 1.45; margin-top: 4px; }
</style>
</head>
<body>

  <section class="card card-front">
    <div class="brand-name">Corbel<br>Insurance Services</div>
    <p class="tagline">Where Trust Meets Coverage</p>
  </section>

  <section class="card card-back">
    <h1 class="holder-name">Dana Whitcomb</h1>
    <p class="holder-license">License # 0M93216</p>
    <p class="holder-title">Producer</p>

    <div class="divider">
      <span class="icon" aria-label="Address">
        <svg viewBox="0 0 16 16"><path d="M8 1.5a4.5 4.5 0 0 0-4.5 4.5C3.5 9.5 8 14.5 8 14.5S12.5 9.5 12.5 6A4.5 4.5 0 0 0 8 1.5z" fill="none" stroke="#fff" stroke-width="1.5"/><circle cx="8" cy="6" r="1.6" fill="#fff"/></svg>
      </span>
    </div>
    <p class="company">Corbel Insurance Services</p>
    <p class="address">27408 Larkmoor Ave Suite 610<br>Sherman Oaks, CA 90217</p>

    <div class="divider">
      <span class="icon-row">
        <span class="icon" aria-label="Phone">
          <svg viewBox="0 0 16 16"><path d="M4.5 2l2 3-1.3 1.3a7 7 0 0 0 4.5 4.5L11 9.5l3 2-1.2 2C7.5 13.5 2.5 8.5 2.5 3.2z" fill="#fff"/></svg>
        </span>
        <span class="icon" aria-label="Email">
          <svg viewBox="0 0 16 16"><rect x="2" y="4" width="12" height="8.5" fill="none" stroke="#fff" stroke-width="1.4"/><path d="M2 4l6 5 6-5" fill="none" stroke="#fff" stroke-width="1.4"/></svg>
        </span>
        <span class="icon" aria-label="Website">
          <svg viewBox="0 0 16 16" fill="none" stroke="#fff" stroke-width="1.3"><circle cx="8" cy="8" r="5.8"/><ellipse cx="8" cy="8" rx="2.5" ry="5.8"/><path d="M2.2 8h11.6"/></svg>
        </span>
      </span>
    </div>
    <p class="phone">(555) 017-3904</p>
    <p class="web">Dana@CorbelInsuranceServices.com<br>CorbelInsuranceServices.com</p>
  </section>

</body>
</html>
```